Business Cards and email stationery for VoiceOver Artist
Cutting Edge Business cards and email stationery for VoiceOver Artist
Use standard fonts
Not sure here?
Bright & Fun-filled
Marcus Dellow
Voiceover
2817 Palmera Ave
Encino CA 91427
(•••NO ADDRESS ON BUSINESS CARDS PLEASE••••)
818-555-2193 Cell
marcus@marcusdellow.example
marcusdellow.example
As 3-D as possible, cutting-edge, creative
1 Should be easy to read
2 Cell number should be listed first!
Uploaded Logo for VoiceOver Artist for Business cards and email Stationery
Logo for VoiceOver Artist v2

```html
<!DOCTYPE html>
<html lang="en">
<head>
<meta charset="utf-8">
<title>Marcus Dellow Voiceover – Stationery</title>
<link rel="stylesheet" href="https://fonts.googleapis.com/css2?family=Exo+2:wght@600;700&family=Open+Sans:wght@400;600&display=swap">
<style>
  :root {
    --bg: #e6e6e6;
    --paper: #ffffff;
    --red: #c4161c;
    --red-deep: #7d0a0e;
    --red-bright: #e0262c;
    --ink: #3a3a3a;
    --ink-soft: #777777;
    --faint: #efe3e3;
  }
  * { box-sizing: border-box; margin: 0; padding: 0; }
  html, body { width: 1200px; height: 936px; overflow: hidden; }
  body { background: var(--bg); position: relative; font-family: "Open Sans", Arial, sans-serif; }

  .piece { position: absolute; overflow: hidden; }

  .brand { position: absolute; display: flex; align-items: center; gap: 8px; }
  .brand-dot { border-radius: 50%; background: var(--red); flex: none; }
  .brand-name {
    font-family: "Exo 2", Arial, sans-serif; font-weight: 700;
    text-transform: uppercase; color: var(--ink); white-space: nowrap; letter-spacing: 0.02em;
  }

  /* Letterhead */
  .letterhead { left: 178px; top: 36px; width: 400px; height: 578px; background: var(--paper); }
  .letterhead .stripe { position: absolute; left: 30px; top: 0; width: 14px; height: 100%;
    background: linear-gradient(90deg, var(--red-deep), var(--red-bright), var(--red-deep)); }
  .letterhead .brand { left: 22px; top: 26px; }
  .letterhead .brand-dot { width: 30px; height: 30px; }
  .letterhead .brand-name { font-size: 17px; }
  .letterhead .watermark { position: absolute; left: 146px; top: 228px; width: 112px; height: 112px;
    border-radius: 50%; background: var(--faint); }
  .contact { position: absolute; font-size: 8px; line-height: 1.6; color: var(--ink-soft); }
  .letterhead .contact { left: 52px; bottom: 12px; }

  /* Folder */
  .folder { left: 634px; top: 36px; width: 426px; height: 580px;
    background: radial-gradient(ellipse at 50% 45%, var(--red-bright) 0%, var(--red) 45%, var(--red-deep) 100%); }
  .folder .brand { left: 30px; top: 268px; gap: 10px; }
  .folder .brand-dot { width: 48px; height: 48px; background: #d9d9d9; }
  .folder .brand-name { font-size: 30px; color: #3b3b3b; }
  .folder .tagline { position: absolute; left: 92px; top: 318px; font-family: "Exo 2", Arial, sans-serif;
    font-weight: 600; font-size: 14px; letter-spacing: 0.55em; color: #f2f2f2; text-transform: uppercase; }

  /* Business cards */
  .card { width: 177px; height: 101px; border-radius: 8px; left: 46px;
    background: linear-gradient(160deg, var(--red-bright), var(--red) 50%, var(--red-deep)); }
  .card-front { top: 655px; }
  .card-back { top: 776px; }
  .card-front .brand { left: 8px; top: 8px; gap: 5px; }
  .card-front .brand-dot { width: 16px; height: 16px; background: #e8e8e8; }
  .card-front .brand-name { font-size: 10px; color: #ffffff; }
  .card-front .contact { left: 28px; top: 32px; font-size: 6px; color: #f4d6d6; line-height: 1.55; }
  .card-front .web { position: absolute; left: 8px; bottom: 6px; font-size: 6px; color: #ffffff; letter-spacing: 0.1em; }
  .card-back .mark { position: absolute; left: 60px; top: 22px; width: 57px; height: 57px;
    border-radius: 50%; background: #e8e8e8; }

  /* Envelopes */
  .envelope { top: 672px; height: 206px; background: var(--paper); }
  .envelope-front { left: 254px; width: 444px; }
  .envelope-front .stripe { position: absolute; left: 24px; top: 0; width: 10px; height: 100%;
    background: linear-gradient(90deg, var(--red-deep), var(--red-bright), var(--red-deep)); }
  .envelope-front .brand { left: 16px; top: 16px; gap: 6px; }
  .envelope-front .brand-dot { width: 26px; height: 26px; }
  .envelope-front .brand-name { font-size: 14px; }
  .envelope-back { left: 741px; width: 426px; }
  .envelope-back .flap { position: absolute; left: 0; top: 0; width: 100%; height: 62px;
    background: linear-gradient(180deg, var(--red-bright), var(--red) 60%, var(--red-deep));
    border-radius: 0 0 10px 10px; }
  .envelope-back .web { position: absolute; left: 0; right: 0; top: 26px; text-align: center;
    font-size: 9px; letter-spacing: 0.3em; color: #ffffff; text-transform: uppercase; font-weight: 600; }
</style>
</head>
<body>

  <section class="piece letterhead" aria-label="Letterhead">
    <div class="stripe"></div>
    <div class="brand"><span class="brand-dot"></span><span class="brand-name">Marcus Dellow</span></div>
    <div class="watermark"></div>
    <p class="contact">818-555-2193 Cell<br>marcus@marcusdellow.example<br>marcusdellow.example</p>
  </section>

  <section class="piece folder" aria-label="Presentation folder">
    <div class="brand"><span class="brand-dot"></span><span class="brand-name">Marcus Dellow</span></div>
    <p class="tagline">Voiceover</p>
  </section>

  <section class="piece card card-front" aria-label="Business card front">
    <div class="brand"><span class="brand-dot"></span><span class="brand-name">Marcus Dellow</span></div>
    <p class="contact">818-555-2193 Cell<br>marcus@marcusdellow.example<br>Voiceover Artist</p>
    <p class="web">www.marcusdellow.example</p>
  </section>

  <section class="piece card card-back" aria-label="Business card back">
    <div class="mark"></div>
  </section>

  <section class="piece envelope envelope-front" aria-label="Envelope front">
    <div class="stripe"></div>
    <div class="brand"><span class="brand-dot"></span><span class="brand-name">Marcus Dellow</span></div>
  </section>

  <section class="piece envelope envelope-back" aria-label="Envelope back">
    <div class="flap"></div>
    <p class="web">www.marcusdellow.example</p>
  </section>

</body>
</html>
```